Website For Custom Home Builder

-Very elegant and simple design as I am a high end custom home builder.
-I build homes $2 million to $10 million range so the website needs to reflect the level of home that I build.
-Attached are photos of homes I have built to use as well as my logo.
-I need final design to be in layered format so my local guy can edit if he needs to.

3 Page Design
1. HomePage:
-logo, some photos,
-“Building beautiful custom homes in Indianapolis for over 20 years”
2. AboutPage:
-Dean Morley has been building stunning custom homes in the Indianpolis area for over 20 years. As a small boutique building company we only build a handful of homes a year in order to offer our clients the personal attention that their homes deserve. It's this attention to detail that makes our client experience and final product something special and unique.
- family photo
3. ContactPage:
-office photo
-317-555-0192
-dean@dmbuildco.example
-415 North Larkwood Dr, Suite 310, Carmel IN 46099

Target Market(s)

Very high end clients looking to build $2 million to $10 million homes.

Industry/Entity Type

Residential high end custom home builder/construction

Coding

Coded - Design and coding required

Number of Pages Required

3 page

Requirements
Must have
• Very simple and elegant design that represents the high end homes that I build.
Nice to have
Should not have
• Should NOT have a lot of clutter or be a very busy page from a design perspective.

```html
<!DOCTYPE html>
<html lang="en">
<head>
<meta charset="utf-8">
<title>Dean Morley Custom Homes</title>
<link href="https://fonts.googleapis.com/css2?family=Poppins:wght@400;500;600&family=Urbanist:wght@500;600&display=swap" rel="stylesheet">
<style>
:root{
  --brown:#8a4a1f;
  --brown-dark:#6e3614;
  --sidebar-top:#7a3e17;
  --sidebar-bot:#a5561f;
  --accent:#e9a445;
  --ink:#1d120c;
  --cream:#faf5f1;
  --band:#1c0e07;
  --muted:#d9d3ce;
  --text:#4a3f39;
}
*{margin:0;padding:0;box-sizing:border-box}
html,body{width:675px;height:1200px;overflow:hidden;background:var(--band)}
body{font-family:"Poppins",sans-serif;color:var(--ink)}
.page{position:relative;width:675px;height:400px;background:var(--cream);overflow:hidden}
.page::after{content:"";position:absolute;left:0;right:0;bottom:0;height:12px;background:var(--band)}
.site-header{position:absolute;left:0;top:0;width:675px;height:33.5px;background:#fff}
.brand{position:absolute;left:33px;top:6px;height:22px;display:flex;align-items:center;gap:6px;color:var(--brown-dark)}
.brand-mark{width:14px;height:14px;background:var(--brown-dark);flex:none}
.brand-name{font-size:7.5px;line-height:9px;font-weight:500;letter-spacing:.6px;text-transform:uppercase;white-space:nowrap}
.nav{position:absolute;top:12px;left:176px}
.nav a{position:absolute;font-size:7.2px;font-weight:500;color:var(--ink);text-decoration:none;white-space:nowrap}
.nav a.active{color:var(--brown)}
.nav a.active::after{content:"";position:absolute;left:0;top:12px;width:13px;height:1px;background:var(--brown)}
.call-btn{position:absolute;left:536px;top:7px;width:105px;height:21px;border-radius:11px;background:var(--brown);color:#fff;font-size:7.4px;font-weight:500;letter-spacing:.4px;display:flex;align-items:center;justify-content:center;gap:7px}
.sidebar{position:absolute;left:0;top:33.5px;width:33.5px;height:354.5px;background:linear-gradient(180deg,var(--sidebar-top),var(--sidebar-bot))}
.sidebar::before{content:"";position:absolute;left:0;right:0;top:131px;height:.5px;background:rgba(255,255,255,.2)}
.sidebar-label{position:absolute;left:16.5px;top:76px;transform:translate(-50%,-50%) rotate(-90deg);font-size:7px;color:var(--accent);white-space:nowrap}
.ruler{position:absolute;left:42px;top:36px;width:6px;height:350px;background:repeating-linear-gradient(180deg,rgba(150,140,130,.55) 0 .5px,transparent .5px 3.5px);z-index:2}
.hero-photo{position:absolute;left:33.5px;top:33.5px;width:641.5px;height:354.5px;background:linear-gradient(180deg,#5c4a3a 0%,#7a5a30 35%,#5a3d22 60%,#2f3320 85%,#25291b 100%)}
.hero-title{position:absolute;left:150px;top:172px;width:375px;text-align:center;font-family:"Urbanist",sans-serif;font-weight:600;font-size:24.5px;line-height:31.5px;color:#fff;text-transform:uppercase}
.slide-count{position:absolute;left:575px;top:342px;display:flex;align-items:center;gap:3px;font-size:12px;color:#fff}
.slide-count .now{color:var(--accent)}
.slide-count i{display:block;width:29px;height:.6px;background:rgba(255,255,255,.8)}
.about-photo{position:absolute;left:62px;top:58px;width:240px;height:246px;background:linear-gradient(180deg,#a9c6dc 0%,#e8dccb 40%,#b98a6d 65%,#6f8a3c 100%)}
.eyebrow{position:absolute;left:330px;top:96px;font-size:8.5px;color:var(--brown);display:flex;align-items:center;gap:4px}
.eyebrow i{display:block;width:30px;height:.6px;background:var(--brown)}
.about-title{position:absolute;left:330px;top:114px;font-family:"Urbanist",sans-serif;font-weight:600;font-size:21px;line-height:25px;color:var(--ink);text-transform:uppercase}
.title-rule{position:absolute;left:330px;top:170px;width:57px;height:2px;background:var(--brown)}
.about-copy{position:absolute;left:330px;top:181.5px;width:240px;font-size:7.2px;line-height:12.2px;color:var(--text)}
.page-num{position:absolute;left:543px;top:264px;display:flex;align-items:center}
.page-num i{display:block;width:60px;height:.6px;background:var(--ink);position:relative}
.page-num i::after{content:"";position:absolute;right:-2px;top:-1.7px;width:4px;height:4px;border-radius:50%;background:var(--ink)}
.page-num span{font-size:33px;font-weight:500;color:var(--muted);line-height:1;margin-left:-8px}
.office-photo{position:absolute;left:67px;top:55px;width:548px;height:255px;background:linear-gradient(160deg,#dfe4e6 0%,#c8d0d2 45%,#55636a 75%,#2a3236 100%)}
.contact-item{position:absolute;top:294px;width:200px;margin-left:-100px;text-align:center;font-size:8px;line-height:12.5px;color:var(--ink)}
.contact-item .icon{width:32px;height:32px;margin:0 auto 13px;border-radius:50%;background:var(--brown);display:flex;align-items:center;justify-content:center}
.contact-item.phone{font-size:9.4px;font-weight:500;letter-spacing:.3px}
</style>
</head>
<body>

<section class="page page-home">
  <div class="hero-photo" role="img" aria-label="Large custom stone and timber home at dusk with lit windows, patio, fire pit and pool"></div>
  <header class="site-header">
    <div class="brand"><span class="brand-mark"></span><span class="brand-name">Dean Morley<br>Custom Homes</span></div>
    <nav class="nav"><a class="active" style="left:0">Home</a><a style="left:54px">About</a><a style="left:107px">Contact</a></nav>
    <div class="call-btn"><svg width="9" height="9" viewBox="0 0 24 24" fill="#fff"><path d="M6.6 10.8a15.1 15.1 0 006.6 6.6l2.2-2.2c.3-.3.7-.4 1-.2 1.1.4 2.3.6 3.6.6.6 0 1 .4 1 1V20c0 .6-.4 1-1 1A17 17 0 013 4c0-.6.4-1 1-1h3.5c.6 0 1 .4 1 1 0 1.3.2 2.5.6 3.6.1.3 0 .7-.2 1z"/></svg>317-555-0192</div>
  </header>
  <aside class="sidebar"><span class="sidebar-label">Home</span></aside>
  <div class="ruler"></div>
  <h1 class="hero-title">Building beautiful custom homes in Indianapolis for over 20 years</h1>
  <div class="slide-count"><span class="now">01</span><i></i><span>08</span></div>
</section>

<section class="page page-about">
  <header class="site-header">
    <div class="brand"><span class="brand-mark"></span><span class="brand-name">Dean Morley<br>Custom Homes</span></div>
    <nav class="nav"><a style="left:0">Home</a><a class="active" style="left:54px">About</a><a style="left:107px">Contact</a></nav>
    <div class="call-btn"><svg width="9" height="9" viewBox="0 0 24 24" fill="#fff"><path d="M6.6 10.8a15.1 15.1 0 006.6 6.6l2.2-2.2c.3-.3.7-.4 1-.2 1.1.4 2.3.6 3.6.6.6 0 1 .4 1 1V20c0 .6-.4 1-1 1A17 17 0 013 4c0-.6.4-1 1-1h3.5c.6 0 1 .4 1 1 0 1.3.2 2.5.6 3.6.1.3 0 .7-.2 1z"/></svg>317-555-0192</div>
  </header>
  <aside class="sidebar"><span class="sidebar-label">About Us</span></aside>
  <div class="ruler"></div>
  <div class="about-photo" role="img" aria-label="Family of four standing on a lawn in front of their new two-storey home"></div>
  <div class="eyebrow">ABOUT <i></i></div>
  <h2 class="about-title">Dean Morley Custom<br>Homes</h2>
  <div class="title-rule"></div>
  <p class="about-copy">Dean Morley has been building stunning custom homes in the Indianpolis area for over 20 years. As a small boutique building company we only build a handful of homes a year in order to offer our clients the personal attention that their homes deserve. It's this attention to detail that makes our client experience and final product something special and unique.</p>
  <div class="page-num"><i></i><span>02</span></div>
</section>

<section class="page page-contact">
  <header class="site-header">
    <div class="brand"><span class="brand-mark"></span><span class="brand-name">Dean Morley<br>Custom Homes</span></div>
    <nav class="nav"><a style="left:0">Home</a><a style="left:54px">About</a><a class="active" style="left:107px">Contact</a></nav>
    <div class="call-btn"><svg width="9" height="9" viewBox="0 0 24 24" fill="#fff"><path d="M6.6 10.8a15.1 15.1 0 006.6 6.6l2.2-2.2c.3-.3.7-.4 1-.2 1.1.4 2.3.6 3.6.6.6 0 1 .4 1 1V20c0 .6-.4 1-1 1A17 17 0 013 4c0-.6.4-1 1-1h3.5c.6 0 1 .4 1 1 0 1.3.2 2.5.6 3.6.1.3 0 .7-.2 1z"/></svg>317-555-0192</div>
  </header>
  <aside class="sidebar"><span class="sidebar-label">Contact us</span></aside>
  <div class="ruler"></div>
  <div class="office-photo" role="img" aria-label="Bright modern office interior with desks, monitors, plants and tall shelving"></div>
  <div class="contact-item phone" style="left:199px">
    <div class="icon"><svg width="12" height="12" viewBox="0 0 24 24" fill="#fff"><path d="M6.6 10.8a15.1 15.1 0 006.6 6.6l2.2-2.2c.3-.3.7-.4 1-.2 1.1.4 2.3.6 3.6.6.6 0 1 .4 1 1V20c0 .6-.4 1-1 1A17 17 0 013 4c0-.6.4-1 1-1h3.5c.6 0 1 .4 1 1 0 1.3.2 2.5.6 3.6.1.3 0 .7-.2 1z"/></svg></div>
    317-555-0192
  </div>
  <div class="contact-item" style="left:337.5px">
    <div class="icon"><svg width="12" height="12" viewBox="0 0 24 24" fill="none" stroke="#fff" stroke-width="2"><rect x="3" y="5" width="18" height="14"/><path d="M3 5l9 8 9-8"/></svg></div>
    dean@dmbuildco.example
  </div>
  <div class="contact-item" style="left:511px">
    <div class="icon"><svg width="12" height="12" viewBox="0 0 24 24" fill="none" stroke="#fff" stroke-width="2"><path d="M12 21s-6-6.2-6-11a6 6 0 0112 0c0 4.8-6 11-6 11z"/><circle cx="12" cy="10" r="2"/></svg></div>
    415 North Larkwood Dr, Suite<br>310, Carmel IN 46099
  </div>
</section>

</body>
</html>
```